Marketing Collateral - Size of Business Card

We are a commercial real estate association that is looking for assistance in developing marketing collateral for our grassroots marketing efforts.

These pieces of collateral will be utilized as leave-behind education/recruiting tools. We envision a folding card the size of (2) business cards connected at the ends. The idea behind this design is that it will "stand up" vertically, so that it will look appealing when placed on a desk.

Attached there is an example of the style of card we are looking for, however in the picture the card is standing up horizontally, we would like it to stand vertically.

Layout of the card:

Outside (Side 1) Portrait - We would like a very striking visual of possibly a skyscraper and the words "Stand Tall Marlow" across it.

Outside (Side 2) Portrait - Simply our logo in the same style as the rest of project

Inside (Side 1 & Side 2) Landscape - Content is not finalized but the vision is to have (3) short points talking about membership to Marlow CPAG.

Attached is an example of the type of custom card we are looking at getting, as well as our current logo. Color choices are completely open, but our standard colors in the past have been dark green, gray, and gunmetal. For this piece, it has been suggested that we utilize red more as that is typically the color of Houston sports teams.

Commercial Real Estate Professionals

Business

Serif
Sans Serif

• Project must be designed within the parameters of a standard business card (3.75 x 2.25) that are attached at the ends. See brief.
• Houses, Apartments, or Homes. We only deal with Commercial Real Estate (office buildings, sky scrapers.)

```html
<!DOCTYPE html>
<html lang="en">
<head>
<meta charset="utf-8">
<title>Stand Tall Marlow – Folding Card</title>
<link href="https://fonts.googleapis.com/css2?family=Mulish:wght@400;600&family=Roboto+Condensed:wght@700&display=swap" rel="stylesheet">
<style>
  :root {
    --backdrop: #dfe2e8;
    --paper: #f4f5f4;
    --forest: #556b5c;
    --forest-deep: #4a5e50;
    --sage: #7f918a;
    --amber: #f0c070;
    --cloud: #f6f4ee;
    --ink-light: #dfe6df;
    --ink-contact: #5b3d4b;
    --watermark: rgba(85, 107, 92, 0.10);
  }
  * { box-sizing: border-box; margin: 0; padding: 0; }
  html, body { width: 1200px; height: 857px; overflow: hidden; }
  body {
    background: var(--backdrop);
    font-family: "Mulish", sans-serif;
    position: relative;
  }

  /* Inside spread: two business cards joined at the fold */
  .inside-spread {
    position: absolute;
    left: 24px; top: 302px;
    width: 840px; height: 252px;
    display: flex;
    box-shadow: 0 10px 30px rgba(40, 50, 60, 0.18);
  }
  .panel { width: 420px; height: 252px; position: relative; overflow: hidden; }

  .panel--contact { background: var(--paper); }
  .contact-watermark {
    position: absolute;
    right: 24px; top: 0;
    height: 252px;
    writing-mode: vertical-rl;
    transform: rotate(180deg);
    display: flex; align-items: center; justify-content: center;
    font-family: "Mulish", sans-serif;
    font-weight: 600;
    font-size: 30px;
    letter-spacing: 3px;
    color: var(--watermark);
    white-space: nowrap;
  }
  .contact-list {
    position: absolute;
    left: 22px; bottom: 20px;
    list-style: none;
    font-size: 11px;
    line-height: 16px;
    color: var(--ink-contact);
  }
  .contact-list li { display: flex; align-items: center; gap: 6px; }
  .contact-icon { width: 10px; height: 10px; flex: none; }

  .panel--benefits {
    background: linear-gradient(135deg, var(--forest) 0%, var(--forest-deep) 100%);
    display: flex; align-items: center; justify-content: center;
    border-left: 1px solid rgba(0,0,0,0.08);
  }
  .benefit-list {
    list-style: none;
    text-align: center;
    color: var(--ink-light);
    font-size: 13px;
    line-height: 20px;
    letter-spacing: 0.3px;
  }

  /* Outside front: portrait card */
  .front-card {
    position: absolute;
    left: 924px; top: 218px;
    width: 252px; height: 420px;
    background: var(--sage);
    overflow: hidden;
    box-shadow: 0 10px 30px rgba(40, 50, 60, 0.2);
  }
  .skyline-art {
    position: absolute; inset: 0;
    background:
      linear-gradient(160deg, var(--amber) 0%, var(--cloud) 22%, var(--sage) 40%, var(--sage) 62%, var(--cloud) 80%, var(--amber) 100%);
  }
  .front-title {
    position: absolute;
    left: 96px; top: 0;
    height: 420px;
    writing-mode: vertical-rl;
    display: flex; align-items: center; justify-content: center;
    font-family: "Roboto Condensed", sans-serif;
    font-weight: 700;
    font-size: 30px;
    letter-spacing: 1px;
    color: #ffffff;
    white-space: nowrap;
    text-transform: uppercase;
  }
</style>
</head>
<body>

  <section class="inside-spread" aria-label="Inside of card">
    <div class="panel panel--contact">
      <div class="contact-watermark" aria-hidden="true">MARLOW CPAG</div>
      <ul class="contact-list">
        <li>
          <svg class="contact-icon" viewBox="0 0 10 10"><rect width="10" height="10" fill="#556b5c"/><path d="M2 3h6v4H2z M2 3l3 2 3-2" fill="none" stroke="#fff" stroke-width="0.8"/></svg>
          info@marlowcpag.org
        </li>
        <li>
          <svg class="contact-icon" viewBox="0 0 10 10"><rect width="10" height="10" fill="#556b5c"/><circle cx="5" cy="5" r="2.8" fill="none" stroke="#fff" stroke-width="0.8"/><path d="M2.2 5h5.6" stroke="#fff" stroke-width="0.8"/></svg>
          www.marlowcpag.org
        </li>
        <li>
          <svg class="contact-icon" viewBox="0 0 10 10"><rect width="10" height="10" fill="#556b5c"/><path d="M3 2.5l1.2 0 .6 1.6-.8.6a4 4 0 0 0 1.6 1.6l.6-.8 1.6.6v1.2a1 1 0 0 1-1.1 1A5.5 5.5 0 0 1 2 3.6a1 1 0 0 1 1-1.1z" fill="#fff"/></svg>
          415 555 0182
        </li>
        <li>
          <svg class="contact-icon" viewBox="0 0 10 10"><rect width="10" height="10" fill="#556b5c"/><rect x="2.5" y="2.5" width="5" height="5" fill="none" stroke="#fff" stroke-width="0.8"/></svg>
          1-541-555-0147
        </li>
      </ul>
    </div>
    <div class="panel panel--benefits">
      <ul class="benefit-list">
        <li>Stay in the Know on the Latest Legislation</li>
        <li>Expand your Network</li>
        <li>Fine Tune your Leadership Skills</li>
        <li>Stay on top of the Latest Trends and Best Practices</li>
        <li>Be Recognized</li>
      </ul>
    </div>
  </section>

  <section class="front-card" aria-label="Outside front of card">
    <div class="skyline-art" role="img" aria-label="Illustration of a skyscraper rising against an amber sky with white clouds"></div>
    <h1 class="front-title">Stand Tall Marlow</h1>
  </section>

</body>
</html>
```